Home Building company needs lettering for our truck doors.

We need lettering for our truck doors and tailgate. We are a home building company in the construction industry. The trucks are gray in color and our company colors are dark blue, gray and white. We'd like the following included in the lettering; Our company name is; Brelmoor Construction Company. My name is Dean P. Brelmoor, Builder/Carpenter/Cabinetmaker. Our phone numbers are; 781-555-0163 and 603-555-0197

Construction

• Times New Roman

```html
<!DOCTYPE html>
<html lang="en">
<head>
<meta charset="utf-8">
<title>Brelmoor Construction Co. — Truck Door Lettering</title>
<link rel="stylesheet" href="https://fonts.googleapis.com/css2?family=Tinos:wght@400;700&display=swap">
<style>
  :root {
    --navy: #020d66;
    --slate: #3d4a50;
    --white: #ffffff;
    --scale: 0.8;
  }
  * { margin: 0; padding: 0; box-sizing: border-box; }
  html, body {
    width: 1200px;
    height: 1200px;
    overflow: hidden;
    background: var(--white);
    font-family: "Tinos", "Times New Roman", serif;
  }
  .canvas { position: relative; width: 1200px; height: 1200px; }
  .panel {
    position: absolute;
    left: 0;
    width: 1200px;
    display: flex;
    flex-direction: column;
    align-items: center;
    text-align: center;
  }
  .panel--white { top: 0; height: 392px; color: var(--navy); background: var(--white); padding-top: 58px; }
  .panel--navy { top: 392px; height: 362px; color: var(--white); background: var(--navy); padding-top: 58px; }
  .panel--slate { top: 793px; height: 361px; color: var(--white); background: var(--slate); padding-top: 58px; }
  .brand-name {
    font-weight: 700;
    font-size: 53px;
    line-height: 1;
    letter-spacing: 1px;
  }
  .brand-tagline {
    font-weight: 400;
    font-size: 24px;
    line-height: 1;
    letter-spacing: 1.3px;
    margin-top: 6px;
  }
  .owner-name {
    font-weight: 700;
    font-size: 28px;
    letter-spacing: 1.5px;
    line-height: 1;
    margin-top: 40px;
  }
  .owner-trades {
    font-weight: 400;
    font-size: 24px;
    letter-spacing: 1.2px;
    line-height: 1;
    margin-top: 14px;
  }
  .phones {
    font-weight: 700;
    font-size: 29px;
    line-height: 1;
    margin-top: 22px;
    letter-spacing: 0.5px;
  }
  .phones .divider { display: inline-block; margin: 0 20px; font-weight: 700; }
</style>
</head>
<body>
<main class="canvas">
  <section class="panel panel--white">
    <h1 class="brand-name">BRELMOOR</h1>
    <p class="brand-tagline">CONSTRUCTION CO.</p>
    <h2 class="owner-name">DEAN P. BRELMOOR</h2>
    <p class="owner-trades">BUILDER | CARPENTER | CABINETMAKER</p>
    <p class="phones">(781) 555-0163<span class="divider">|</span>(603) 555-0197</p>
  </section>
  <section class="panel panel--navy">
    <h1 class="brand-name">BRELMOOR</h1>
    <p class="brand-tagline">CONSTRUCTION CO.</p>
    <h2 class="owner-name">DEAN P. BRELMOOR</h2>
    <p class="owner-trades">BUILDER | CARPENTER | CABINETMAKER</p>
    <p class="phones">(781) 555-0163<span class="divider">|</span>(603) 555-0197</p>
  </section>
  <section class="panel panel--slate">
    <h1 class="brand-name">BRELMOOR</h1>
    <p class="brand-tagline">CONSTRUCTION CO.</p>
    <h2 class="owner-name">DEAN P. BRELMOOR</h2>
    <p class="owner-trades">BUILDER | CARPENTER | CABINETMAKER</p>
    <p class="phones">(781) 555-0163<span class="divider">|</span>(603) 555-0197</p>
  </section>
</main>
</body>
</html>
```